QuillMark Business Cards

I need a business card designed for QuillMark. To get an idea of what we do please visit https://formvault.example/para-creadores-3

```html
<!DOCTYPE html>
<html lang="en">
<head>
<meta charset="utf-8">
<title>QuillMark — Business Card</title>
<link rel="stylesheet" href="https://fonts.googleapis.com/css2?family=Raleway:wght@400;500&display=swap">
<style>
  :root {
    --card-bg: #1f2227;
    --ink-light: #ffffff;
    --accent-orange: #e08a14;
    --accent-deep: #b86d0c;
  }
  * { margin: 0; padding: 0; box-sizing: border-box; }
  html, body {
    width: 1200px;
    height: 699px;
    overflow: hidden;
    background: var(--card-bg);
  }
  .card {
    position: relative;
    width: 1200px;
    height: 699px;
    background: var(--card-bg);
    overflow: hidden;
    font-family: "Raleway", sans-serif;
  }
  .brand-mark {
    position: absolute;
    left: 150px;
    top: 262px;
    width: 58px;
    height: 58px;
    border-radius: 50%;
    background: var(--accent-orange);
  }
  .brand-name {
    position: absolute;
    left: 292px;
    top: 256px;
    font-size: 64px;
    font-weight: 400;
    letter-spacing: 0.2em;
    line-height: 1;
    color: var(--ink-light);
    white-space: nowrap;
  }
  .tagline-row {
    position: absolute;
    left: 295px;
    top: 337px;
    display: flex;
    align-items: center;
    gap: 8px;
  }
  .tagline {
    font-size: 19px;
    font-weight: 500;
    letter-spacing: 0.32em;
    color: var(--accent-orange);
    line-height: 1;
    white-space: nowrap;
  }
  .tagline-rule {
    width: 190px;
    height: 2px;
    background: var(--ink-light);
  }
  .facet-field {
    position: absolute;
    right: 0;
    bottom: 0;
    width: 700px;
    height: 440px;
    background:
      radial-gradient(ellipse 90% 95% at 100% 100%,
        var(--accent-orange) 0%,
        var(--accent-orange) 30%,
        rgba(184, 109, 12, 0.75) 55%,
        rgba(184, 109, 12, 0.25) 78%,
        rgba(31, 34, 39, 0) 100%);
  }
</style>
</head>
<body>
  <div class="card">
    <div class="facet-field" role="img" aria-label="Field of small orange triangles dissolving from the bottom right corner into the dark background"></div>
    <div class="brand-mark" aria-hidden="true"></div>
    <h1 class="brand-name">QUILLMARK</h1>
    <div class="tagline-row">
      <p class="tagline">DIGITAL NOTARY</p>
      <span class="tagline-rule" aria-hidden="true"></span>
    </div>
  </div>
</body>
</html>
```